Need to create a website for a luxury custom home builder in Phoenix USA. Looking forward for some creative designs including a full page video intro on homepage and should show up pretty luxurious.

```html
<!DOCTYPE html>
<html lang="en">
<head>
<meta charset="utf-8">
<title>Crestvale Homes | Luxury Custom Homes, Phoenix</title>
<link href="https://fonts.googleapis.com/css2?family=Montserrat:wght@300;400;500;600;700&display=swap" rel="stylesheet">
<style>
:root{
  --gold:#b4a47c;
  --ink:#2b2b2b;
  --sand:#f2f0eb;
  --sand-light:#f6f4f0;
  --line:#e4e1da;
  --black:#0b0b0b;
  --white:#fff;
}
*{margin:0;padding:0;box-sizing:border-box}
html,body{width:1200px;height:3725px;overflow:hidden}
body{position:relative;font-family:"Montserrat",sans-serif;color:var(--ink);background:var(--white)}
.abs{position:absolute}
.photo{position:absolute;display:block}
.section-title{position:absolute;left:0;width:1200px;text-align:center;color:var(--gold);font-weight:400;font-size:18px;letter-spacing:.5px;text-transform:uppercase}
.section-lead{position:absolute;left:0;width:1200px;text-align:center;font-size:10.5px;line-height:19px}
.btn-gold{position:absolute;background:var(--gold);color:var(--white);font-size:10px;letter-spacing:2px;text-transform:uppercase;display:flex;align-items:center;justify-content:center}

/* hero video intro */
.hero-video{position:absolute;left:0;top:0;width:1200px;height:636px;background:linear-gradient(180deg,#8fb2c9 0%,#d6cfc0 30%,#c9a987 48%,#8a6d52 64%,#2f6f7d 80%,#5a7f84 100%)}
.hero-shade{position:absolute;left:0;top:0;width:420px;height:636px;background:linear-gradient(90deg,rgba(40,36,30,.85) 0%,rgba(60,54,44,.55) 60%,rgba(60,54,44,0) 100%)}
.brand-top{position:absolute;top:14px;left:468px;display:flex;align-items:center;gap:10px;color:var(--white)}
.brand-mark{width:34px;height:34px;border:2px solid var(--white);border-radius:50%}
.brand-name{font-weight:600;font-size:24px;letter-spacing:1px;line-height:1}
.brand-name small{display:block;font-size:12px;letter-spacing:6px;margin-top:3px}
.top-contact{position:absolute;top:31px;font-size:10px;color:var(--white);display:flex;align-items:center;gap:6px}
.burger{position:absolute;left:1022px;top:30px;width:22px}
.burger span{display:block;height:1px;background:var(--white);margin-bottom:5px}
.hero-title{position:absolute;left:48px;top:236px;color:var(--white);font-size:18px;font-weight:400;letter-spacing:2.5px;line-height:25px;text-transform:uppercase}
.hero-sub{position:absolute;left:48px;top:347px;color:var(--white);font-size:11px;line-height:19px}
.btn-white{position:absolute;top:409px;height:35px;background:var(--white);color:var(--ink);font-size:10px;letter-spacing:1.8px;display:flex;align-items:center;justify-content:center;text-transform:uppercase}

/* search */
.search{position:absolute;left:155px;top:607px;width:890px;height:70px;background:var(--white);box-shadow:0 2px 8px rgba(0,0,0,.08);border:1px solid var(--line)}
.field{position:absolute;top:18px}
.field-label{font-size:8.5px;color:var(--gold);text-transform:uppercase;letter-spacing:.3px}
.field-value{font-size:10px;margin-top:8px;display:flex;align-items:center;gap:6px}
.field-sep{position:absolute;top:12px;width:1px;height:46px;background:var(--line)}
.radio{width:8px;height:8px;border-radius:50%;border:1px solid #ccc;display:inline-block}
.radio.on{background:var(--gold);border-color:var(--gold)}
.search-btn{position:absolute;left:826px;top:6px;width:58px;height:56px;background:var(--gold);display:flex;align-items:center;justify-content:center}

/* categories */
.cat-label{position:absolute;text-align:center;width:267px}
.cat-label b{display:block;font-weight:400;color:var(--gold);font-size:14px;text-transform:uppercase;letter-spacing:.5px}
.cat-label span{font-size:10px}

/* agents */
.agents-band{position:absolute;left:0;top:1197px;width:1200px;height:470px;background:var(--sand)}
.agents-title{position:absolute;left:610px;top:1353px;color:var(--gold);font-size:18px;font-weight:400;text-transform:uppercase}
.agents-text{position:absolute;left:610px;top:1398px;width:395px;font-size:10.5px;line-height:19px}

/* listings */
.listing{position:absolute;top:1843px;width:284px;height:366px;border:1px solid var(--line);background:var(--white)}
.listing .photo{left:-1px;top:-1px;width:284px;height:171px}
.listing-tag{position:absolute;top:191px;width:100%;text-align:center;color:var(--gold);font-size:8.5px;font-weight:600;letter-spacing:1px;text-transform:uppercase}
.listing-title{position:absolute;top:207px;width:100%;text-align:center;font-size:11px;line-height:19px;text-transform:uppercase}
.listing-body{position:absolute;top:268px;left:14px;right:14px;text-align:center;font-size:9px;line-height:19px}
.read-more{position:absolute;width:100%;text-align:center;color:var(--gold);font-size:9.5px;letter-spacing:2px;text-transform:uppercase}

/* quality */
.quality{position:absolute;left:155px;top:2683px;width:890px;height:303px;background:var(--sand-light)}
.quality h2{margin-top:36px;text-align:center;color:var(--gold);font-weight:400;font-size:18px;line-height:26px;text-transform:uppercase}
.quality p{text-align:center;font-size:10.5px;line-height:19px;margin:16px 60px 0}
.quality .note{color:var(--gold);font-size:9px;margin-top:16px}

/* blog */
.blog{position:absolute;top:3149px;width:436px;height:211px;border:1px solid var(--line);background:var(--white)}
.blog-text{position:absolute;left:0;top:0;width:218px;height:100%;text-align:center}
.blog-title{margin-top:50px;font-size:10.5px;line-height:19px;text-transform:uppercase;padding:0 18px}
.blog-body{margin-top:20px;font-size:9px;line-height:19px;padding:0 18px}

/* brochures & newsletter */
.band{position:absolute;left:0;top:3411px;width:1200px;height:82px;background:var(--sand)}

/* footer */
.footer{position:absolute;left:0;top:3493px;width:1200px;height:232px;background:var(--black);color:var(--white)}
.foot-brand{position:absolute;left:155px;top:16px;display:flex;align-items:center;gap:14px}
.foot-brand .ring{width:56px;height:56px;border:3px solid #fff;border-radius:50%}
.foot-brand .name{font-size:38px;font-weight:600;letter-spacing:1px;line-height:1}
.foot-brand .name small{display:block;font-size:17px;letter-spacing:8px;margin-top:4px}
.foot-nav{position:absolute;top:54px;right:155px;display:flex;gap:20px;font-size:10px;text-transform:uppercase}
.foot-small{font-size:9.5px}
.social{position:absolute;top:110px;width:9px;height:9px;border-radius:50%;background:#fff}
</style>
</head>
<body>

<!-- full-screen video intro -->
<section class="hero-video" role="img" aria-label="Full-screen intro video: luxury custom home in the Phoenix desert, pool terrace at sunset with Camelback Mountain behind"></section>
<div class="hero-shade"></div>
<div class="brand-top"><span class="brand-mark"></span><span class="brand-name">CRESTVALE<small>HOMES</small></span></div>
<div class="top-contact" style="left:728px">
  <svg width="10" height="10" viewBox="0 0 24 24" fill="none" stroke="#fff" stroke-width="2"><path d="M22 16.9v3a2 2 0 0 1-2.2 2 19.8 19.8 0 0 1-8.6-3.1 19.5 19.5 0 0 1-6-6A19.8 19.8 0 0 1 2.1 4.2 2 2 0 0 1 4.1 2h3a2 2 0 0 1 2 1.7c.1 1 .4 1.9.7 2.8a2 2 0 0 1-.5 2.1L8 9.9a16 16 0 0 0 6 6l1.3-1.3a2 2 0 0 1 2.1-.4c.9.3 1.8.6 2.8.7a2 2 0 0 1 1.7 2z"/></svg>
  +1 (602) 555-0148</div>
<div class="top-contact" style="left:858px">
  <svg width="11" height="9" viewBox="0 0 24 18" fill="none" stroke="#fff" stroke-width="2"><rect x="1" y="1" width="22" height="16"/><path d="M1 1l11 9 11-9"/></svg>
  hello@crestvale-homes.com</div>
<div class="burger"><span></span><span></span><span></span></div>

<h1 class="hero-title">Exclusivity. Lovely<br>family home with<br>swimming pool, Scottsdale</h1>
<p class="hero-sub">Luxury Custom Homes, Design<br>and Build. Phoenix, Arizona</p>
<div class="btn-white" style="left:48px;width:137px">See property</div>
<div class="btn-white" style="left:215px;width:139px">All properties</div>

<!-- search -->
<div class="search">
  <div class="field" style="left:22px"><div class="field-label">Search by reference</div><div class="field-value">Keywords</div></div>
  <div class="field-sep" style="left:231px"></div>
  <div class="field" style="left:245px;width:125px"><div class="field-label">Regions</div><div class="field-value" style="justify-content:space-between">Select <span>⌄</span></div></div>
  <div class="field-sep" style="left:382px"></div>
  <div class="field" style="left:396px;width:105px"><div class="field-label">Type</div><div class="field-value" style="justify-content:space-between">Estates <span>⌄</span></div></div>
  <div class="field-sep" style="left:517px"></div>
  <div class="field" style="left:530px"><div class="field-label">Select</div><div class="field-value"><span class="radio on"></span>Buy&nbsp;&nbsp;&nbsp;<span class="radio"></span>Build</div></div>
  <div class="field-sep" style="left:658px"></div>
  <div class="field" style="left:671px;width:135px"><div class="field-label">Price range</div><div class="field-value" style="justify-content:space-between">$1 - $24,000,000 <span>USD ⌄</span></div></div>
  <div class="search-btn"><svg width="20" height="20" viewBox="0 0 24 24" fill="none" stroke="#fff" stroke-width="1.5"><circle cx="10.5" cy="10.5" r="7"/><path d="M15.5 15.5L21 21"/></svg></div>
</div>

<!-- categories -->
<h2 class="section-title" style="top:745px">Categories</h2>
<p class="section-lead" style="top:789px">Make your search easier! We have classified our homes to help find<br>directly the properties corresponding to your criteria.</p>

<div class="photo" style="left:48px;top:859px;width:266px;height:218px;background:linear-gradient(180deg,#b9a48a 0%,#d4c3a8 35%,#2f7d98 70%,#1e5e78 100%)" role="img" aria-label="Infinity pool terrace with desert mountain view"></div>
<div class="cat-label" style="left:48px;top:1090px"><b>Luxury estates</b><span>Fine custom homes of Arizona</span></div>

<div class="photo" style="left:327px;top:885px;width:267px;height:218px;background:linear-gradient(180deg,#ece8e1 0%,#d8d0c4 45%,#a39a8d 80%,#7c766d 100%)" role="img" aria-label="Bright great room with floor-to-ceiling windows"></div>
<div class="cat-label" style="left:327px;top:1117px"><b>Golf course</b><span>Homes on the fairway</span></div>

<div class="photo" style="left:607px;top:859px;width:268px;height:218px;background:linear-gradient(180deg,#d8d6d0 0%,#b9b5ad 45%,#5d5f66 70%,#a57d4f 100%)" role="img" aria-label="Primary bedroom with wooden bed and pendant lights"></div>
<div class="cat-label" style="left:607px;top:1090px"><b>Desert</b><span>Best mountain views</span></div>

<div class="photo" style="left:888px;top:885px;width:267px;height:218px;background:linear-gradient(180deg,#b7a487 0%,#8d7b66 40%,#4b8fa0 75%,#2e6f83 100%)" role="img" aria-label="Pool deck with loungers beside a stone wall"></div>
<div class="cat-label" style="left:888px;top:1117px"><b>Custom builds</b><span>Luxury Lifestyle</span></div>

<!-- agents -->
<section class="agents-band"></section>
<div class="photo" style="left:155px;top:1319px;width:120px;height:120px;background:linear-gradient(160deg,#3f6b38,#2a4a26)" role="img" aria-label="Team member portrait"></div>
<div class="photo" style="left:293px;top:1349px;width:119px;height:120px;background:linear-gradient(160deg,#3c6936,#27452a)" role="img" aria-label="Team member portrait"></div>
<div class="photo" style="left:429px;top:1291px;width:120px;height:119px;background:linear-gradient(160deg,#44713a,#2c4c28)" role="img" aria-label="Team member portrait"></div>
<div class="photo" style="left:155px;top:1456px;width:120px;height:120px;background:linear-gradient(160deg,#3e6a37,#284727)" role="img" aria-label="Team member portrait"></div>
<div class="photo" style="left:292px;top:1486px;width:120px;height:119px;background:linear-gradient(160deg,#406d38,#223e24)" role="img" aria-label="Team member portrait"></div>
<div class="photo" style="left:429px;top:1427px;width:120px;height:119px;background:linear-gradient(160deg,#3d6a36,#294828)" role="img" aria-label="Team member portrait"></div>
<h2 class="agents-title">Our builders across Arizona !</h2>
<p class="agents-text">Meet the team! We are all experts in our field. With different professional backgrounds such as architecture, finance, interiors, landscaping or real estate development, we also all have a solid experience of custom home builds to assist you in the design of your home or in your research. All this with an exceptional customer service.</p>
<div class="btn-gold" style="left:610px;top:1520px;width:140px;height:36px">Our team</div>

<!-- featured -->
<h2 class="section-title" style="top:1734px">Featured listings</h2>
<p class="section-lead" style="top:1780px">A doubt about what you are looking for? Let yourself be assisted with some random proposals or contact us<br>directly. We will help you clarify your search and we will send you targeted home suggestions.</p>

<article class="listing" style="left:155px">
  <div class="photo" style="background:linear-gradient(180deg,#7a5a45 0%,#b69b7e 45%,#e7e2d9 75%,#9a8a74 100%)" role="img" aria-label="Renovated hacienda hallway with art and antiques"></div>
  <div class="listing-tag">AZ 85018 Arcadia</div>
  <div class="listing-title">Outstanding renovated<br>hacienda house</div>
  <div class="listing-body">Nestled in the heart of Arcadia at the foot of Camelback Mountain, this superb custom home built on a lot of 1.2 acres enjoys a private and quiet setting...</div>
  <div class="read-more" style="top:331px">Read more →</div>
</article>
<article class="listing" style="left:457px">
  <div class="photo" style="background:linear-gradient(180deg,#7fa9d6 0%,#d3c1a2 35%,#3da6cf 65%,#8a7a5e 100%)" role="img" aria-label="Desert estate with pool and mountain backdrop"></div>
  <div class="listing-tag">AZ 85253 Paradise Valley</div>
  <div class="listing-title">Beautiful desert estate<br>with pool and guest casita</div>
  <div class="listing-body">Located on a hillside lot in Paradise Valley, this estate is exceptional for its city light views and rare, sought-after features...</div>
  <div class="read-more" style="top:331px">Read more →</div>
</article>
<article class="listing" style="left:760px">
  <div class="photo" style="background:linear-gradient(180deg,#8fa0b5 0%,#d9c7a6 40%,#7f9a5a 70%,#5f7a3a 100%)" role="img" aria-label="Family villa with large lawn and palm trees"></div>
  <div class="listing-tag">AZ 85255 North Scottsdale</div>
  <div class="listing-title">Exclusivity: beautiful family villa<br>with swimming pool</div>
  <div class="listing-body">Located in the prime area of North Scottsdale, this elegant villa is built on a lot of about 2 acres, sheltered from all nuisances and prying eyes...</div>
  <div class="read-more" style="top:331px">Read more →</div>
</article>
<div class="btn-gold" style="left:477px;top:2234px;width:246px;height:36px">View all featured properties</div>

<!-- quality -->
<div class="photo" style="left:0;top:2318px;width:1200px;height:470px;background:linear-gradient(180deg,#9fc0dc 0%,#c9a987 22%,#2fb7cf 40%,#69cbd8 55%,#d9dcdc 72%,#bfc2c3 100%)" role="img" aria-label="Open-air lounge with sofas facing an infinity pool and desert mountains"></div>
<section class="quality">
  <h2>We provide unrivalled quality<br>for more than 15 years</h2>
  <p>Since its creation in 2006, Crestvale Homes has built an unrivalled portfolio of luxury custom homes across Phoenix, Scottsdale and Paradise Valley. The experience of our builders guarantees you a home crafted to the finest detail, our designers make every space your own. Our expertise allows every client to benefit from the best land and the best advice, making your build a unique experience.</p>
  <p class="note">FOR CONFIDENTIALITY REASONS, 30 TO 40% OF OUR HOMES ARE NOT LISTED ON THIS WEBSITE. PLEASE CALL US FOR MORE INFORMATION.</p>
</section>
<div class="btn-gold" style="left:529px;top:2910px;width:141px;height:36px">About us</div>

<!-- blog -->
<h2 class="section-title" style="top:3016px">Lastest blog articles</h2>
<p class="section-lead" style="top:3062px">Interested in custom homes? We are always looking for talented people and new partners. And if you are not<br>ready to take the step, here is a selection of articles on our industry.</p>

<article class="blog" style="left:155px">
  <div class="blog-text">
    <div class="blog-title">Inflation: implications for real estate</div>
    <div class="blog-body">The relationship between real estate and inflation is more nuanced than conventional wisdom suggests</div>
    <div class="read-more" style="top:184px">Read more →</div>
  </div>
  <div class="photo" style="left:218px;top:-1px;width:218px;height:211px;background:linear-gradient(135deg,#12b8d4,#0aa5c4)" role="img" aria-label="Illustration of a person holding back a falling arrow"></div>
</article>
<article class="blog" style="left:609px">
  <div class="blog-text">
    <div class="blog-title">The world of women and work</div>
    <div class="blog-body">Women make up 50% of the global population but less than 40% of the global labour force...</div>
    <div class="read-more" style="top:184px">Read more →</div>
  </div>
  <div class="photo" style="left:218px;top:-1px;width:218px;height:211px;background:linear-gradient(135deg,#a7a8d8,#8d8fcf)" role="img" aria-label="Illustration of a woman on a video call at a desk"></div>
</article>

<!-- brochures / newsletter -->
<section class="band"></section>
<div class="abs" style="left:155px;top:3437px;color:var(--gold);font-size:18px;text-transform:uppercase">Brochures</div>
<div class="abs" style="left:155px;top:3461px;font-size:9.5px">The latest market news and partner research reports</div>
<div class="photo" style="left:434px;top:3427px;width:68px;height:43px;background:linear-gradient(180deg,#9bc3d8,#d9cdb8)" role="img" aria-label="Brochure cover"></div>
<div class="photo" style="left:509px;top:3427px;width:68px;height:43px;background:linear-gradient(180deg,#b8c2c8,#e7e4de)" role="img" aria-label="Brochure cover"></div>
<div class="abs" style="left:620px;top:3441px;color:var(--gold);font-size:18px;text-transform:uppercase">Newsletter</div>
<div class="abs" style="left:762px;top:3435px;width:185px;height:35px;background:var(--white);display:flex;align-items:center;gap:8px;padding-left:12px;font-size:10px">
  <svg width="11" height="9" viewBox="0 0 24 18" fill="none" stroke="#999" stroke-width="2"><rect x="1" y="1" width="22" height="16"/><path d="M1 1l11 9 11-9"/></svg>Enter your email...</div>
<div class="btn-gold" style="left:947px;top:3435px;width:98px;height:35px;font-size:9.5px">Subscribe</div>

<!-- footer -->
<footer class="footer">
  <div class="foot-brand"><span class="ring"></span><span class="name">CRESTVALE<small>HOMES</small></span></div>
  <nav class="foot-nav"><span>Home</span><span>Our company</span><span>Partners</span><span>Custom homes</span><span>Blog</span><span>Contact</span></nav>
  <div class="abs foot-small" style="left:786px;top:75px">☎ +1 (602) 555-0148</div>
  <div class="abs foot-small" style="left:915px;top:75px">✉ hello@crestvale-homes.com</div>
  <p class="abs" style="left:155px;top:108px;width:440px;font-size:9px;line-height:19px">Crestvale Homes specializes in designing, building and selling exceptional custom homes and does not deal with anything outside this very specific segment. We can thus guarantee...</p>
  <div class="abs" style="left:155px;top:150px;color:var(--gold);font-size:8.5px">READ MORE</div>
  <span class="social" style="left:979px"></span>
  <span class="social" style="left:1005px"></span>
  <span class="social" style="left:1034px"></span>
  <span class="abs" style="left:1008px;top:132px;width:37px;height:36px;background:var(--gold)"></span>
  <div class="abs" style="left:155px;top:180px;width:890px;height:1px;background:#333"></div>
  <div class="abs" style="left:155px;top:200px;font-size:8.5px">Copyright © 2022 crestvale-homes.com - All rights reserved</div>
  <div class="abs" style="right:155px;top:200px;font-size:8.5px;display:flex;gap:10px"><span>Privacy Policy</span><span>Term &amp; Condition</span><span>Legal Notice</span></div>
</footer>

</body>
</html>
```